Update existing website to a one page design.

Combine a multi page website into a single page design.
Existing site is at ac.tallowmerecover (dot) com.
Rearrange elements as needed to create a modem look.
Not every element / all of the text need to be kept, design should be flexible enough to allow for new text (of different length) to be used.
Site should have a clear calls to action, such as get a quote and contact us.
Ability, call to action, to switch to Russian should be clearly visible near the top, translation will not be done by vextra, thus attribution is not needed.
Unused features (such as blog) should be dropped.
Images, besides logos, can be brand new.
Site should adhere to standard design practices (such as grid) and ideally be compatible with existing framework (such as bootstrap).
Coding of the website will likely be done by the winning bidder as a separate project.

```html
<!DOCTYPE html>
<html lang="en">
<head>
<meta charset="utf-8">
<title>Tallowmere Cover – Insurance</title>
<link href="https://fonts.googleapis.com/css2?family=Montserrat:wght@500;600;700;800&family=Poppins:wght@400;500;600&display=swap" rel="stylesheet">
<style>
:root{
  --navy:#0b3c93;
  --navy-dark:#08306f;
  --yellow:#fcc400;
  --yellow-soft:#fff4c9;
  --yellow-faint:#fffaf0;
  --ink:#2b2b2b;
  --muted:#5d6270;
  --line:#d9dde6;
  --bg-soft:#f4f7fd;
  --white:#ffffff;
}
*{box-sizing:border-box;margin:0;padding:0}
html,body{width:1200px;height:4823px;overflow:hidden}
body{position:relative;background:var(--white);font-family:"Poppins",sans-serif;color:var(--ink)}
.sec{position:absolute;left:0;width:1200px}
.abs{position:absolute}
h1,h2,h3,h4,.heading{font-family:"Montserrat",sans-serif}
.btn{position:absolute;display:flex;align-items:center;justify-content:center;gap:12px;border-radius:30px;font-family:"Montserrat",sans-serif;font-weight:600;font-size:13px;letter-spacing:.3px;text-transform:uppercase}
.btn-navy{background:var(--navy);color:var(--white)}
.btn-yellow{background:var(--yellow);color:var(--navy)}
.arrow-ring{width:26px;height:26px;border-radius:50%;border:2px solid var(--yellow);display:flex;align-items:center;justify-content:center}
.btn-yellow .arrow-ring{border-color:var(--navy)}
.arrow-ring svg{width:12px;height:12px}

/* header */
.topbar{top:0;height:67px;background:var(--navy)}
.brand{position:absolute;display:flex;align-items:center;gap:10px;color:var(--white);font-family:"Montserrat",sans-serif;font-weight:700;font-size:16px;line-height:20px;letter-spacing:.2px}
.brand-square{width:36px;height:36px;border:3px solid var(--yellow);border-radius:6px}
.call{left:822px;top:14px;display:flex;align-items:center;gap:10px}
.call-icon{width:34px;height:34px;border-radius:50%;border:2px solid var(--yellow);display:flex;align-items:center;justify-content:center}
.call small{display:block;color:var(--yellow);font-size:11px;line-height:14px}
.call b{display:block;color:var(--white);font-family:"Montserrat",sans-serif;font-size:16px;line-height:20px}
.langs{left:1000px;top:17px;display:flex;gap:5px}
.lang{width:32px;height:32px;border-radius:50%;overflow:hidden;border:2px solid var(--white)}
.navbar{top:67px;height:45px;background:var(--white);border-bottom:1px solid #eceff4}
.nav{position:absolute;left:60px;top:0;height:45px;display:flex;align-items:center;font-size:11.5px;color:var(--ink)}
.nav a{display:flex;align-items:center;height:45px;padding:0 12px;color:inherit;text-decoration:none}
.nav a.active{background:var(--yellow);color:var(--navy);padding:0 22px;margin-right:12px}
.nav-cta{left:986px;top:5px;width:154px;height:35px;background:var(--yellow);color:var(--navy);font-size:12px;font-weight:500;display:flex;align-items:center;justify-content:center}

/* hero */
.hero{top:112px;height:600px;overflow:hidden}
.hero-glow{left:-130px;top:-90px;width:330px;height:330px;border-radius:50%;background:var(--yellow-faint)}
.hero-kicker{left:60px;top:140px;font-family:"Montserrat",sans-serif;font-weight:800;font-size:38px;line-height:48px;color:var(--yellow);-webkit-text-stroke:1px #c98f00}
.hero-title{left:60px;top:236px;font-size:41px;font-weight:800;color:var(--navy);letter-spacing:1px}
.hero-text{left:60px;top:290px;width:360px;font-size:13.5px;line-height:22px;color:var(--ink)}
.follow{left:60px;top:514px;display:flex;align-items:center;gap:10px;font-size:10px}
.follow i{display:block;width:56px;height:1px;background:#888}
.social-dot{width:30px;height:30px;border:1.5px solid var(--navy);border-radius:50%}

/* quote box */
.quote{left:225px;top:786px;width:750px;height:200px;border:2px solid var(--navy);border-radius:24px}
.quote-head{position:absolute;left:160px;top:-14px;width:430px;background:var(--white);text-align:center;color:var(--navy);font-weight:700}
.quote-head .l1{font-size:20px;line-height:30px}
.quote-head .l2{font-size:16px;line-height:24px}
.dot{position:absolute;width:12px;height:12px;border-radius:50%;background:var(--yellow);top:8px}
.quote p{position:absolute;left:140px;top:62px;width:470px;text-align:center;font-size:11.5px;line-height:20px;color:var(--muted)}
.select{position:absolute;left:172px;top:120px;width:406px;height:41px;border:1px solid var(--line);border-radius:4px;font-size:11px;color:var(--muted);display:flex;align-items:center;padding-left:18px}
.select span{position:absolute;right:0;top:-1px;width:38px;height:41px;background:var(--yellow);border-radius:0 4px 4px 0;display:flex;align-items:center;justify-content:center}

/* welcome */
.welcome{top:1080px;height:480px}
.welcome-photo{left:162px;top:44px;width:432px;height:338px;border-radius:58% 42% 48% 52% / 44% 56% 44% 56%;background:linear-gradient(135deg,#8a6f57,#c2b4a4 45%,#e4e6ea);transform:rotate(-8deg)}
.w-dot1{left:266px;top:38px;width:32px;height:32px;border-radius:50%;background:#ffe27a}
.w-dot2{left:425px;top:334px;width:76px;height:76px;border-radius:50%;background:var(--yellow-soft)}
.kicker{font-size:13px;color:var(--yellow)}
.welcome .kicker{left:691px;top:14px}
.welcome h2{left:691px;top:40px;font-size:30px;line-height:38px;font-weight:700;color:var(--navy)}
.welcome .body{left:691px;width:370px;font-size:11.3px;line-height:19.5px;color:var(--muted)}

/* services */
.services{top:1554px;height:842px;background:linear-gradient(180deg,var(--bg-soft),#fafbfe 80%,var(--white))}
.services h2{left:0;width:1200px;top:88px;text-align:center;font-size:30px;font-weight:700;color:var(--navy)}
.services .sub{left:0;width:1200px;top:130px;text-align:center;font-size:13px}
.card{position:absolute;width:262px;height:225px;background:var(--white);border-radius:6px;box-shadow:0 6px 22px rgba(11,60,147,.08);padding:0 24px}
.card.featured{background:var(--yellow)}
.card .icon{position:absolute;left:22px;top:18px;width:56px;height:56px}
.card.featured .icon{left:-6px;top:-20px;width:84px;height:84px;border-radius:50%;background:var(--white);display:flex;align-items:center;justify-content:center}
.card h3{position:absolute;left:24px;top:94px;font-size:13px;font-weight:600;color:var(--ink)}
.card p{position:absolute;left:24px;top:120px;width:216px;font-size:11px;line-height:19px;color:var(--muted)}
.card.featured p{color:#4a3b00}
.card .more{position:absolute;right:16px;top:196px;font-size:11px;color:var(--navy);text-decoration:underline;font-weight:500}
.cta-bar{left:264px;top:769px;width:668px;height:45px;border-radius:24px;background:var(--navy);color:var(--white);font-family:"Montserrat",sans-serif;font-weight:600;font-size:13.5px}
.cta-bar span{position:absolute;top:14px}
.or{position:absolute;left:300px;top:-12px;width:68px;height:68px;border-radius:50%;background:var(--white);display:flex;align-items:center;justify-content:center}
.or b{width:56px;height:56px;border-radius:50%;background:var(--yellow);border:3px solid var(--navy);display:flex;align-items:center;justify-content:center;color:var(--navy);font-size:18px}

/* carriers */
.carriers{top:2396px;height:420px}
.carriers h2{left:0;width:1200px;top:62px;text-align:center;font-size:21px;line-height:32px;font-weight:700;color:var(--navy)}
.tile{position:absolute;width:134px;height:131px;background:var(--yellow-soft);display:flex;align-items:center;justify-content:center;text-align:center;font-family:"Montserrat",sans-serif;font-weight:700;font-size:16px;line-height:21px;color:var(--navy);padding:8px}

/* group health */
.group{top:2879px;height:466px}
.group-photo{left:0;top:0;width:825px;height:466px;background:linear-gradient(90deg,#c9cfd8,#e9ecef 40%,#d8cfc6 75%,#b9b0a7)}
.group-card{left:694px;top:56px;width:334px;height:345px;background:var(--white);box-shadow:0 8px 30px rgba(0,0,0,.1);text-align:center}
.group-card h2{position:absolute;left:0;width:334px;top:50px;font-size:31px;line-height:36px;font-weight:700;color:var(--navy)}
.group-card p{position:absolute;left:38px;width:258px;top:182px;font-size:11.5px;line-height:19px;color:var(--muted)}

/* doctor */
.doctor{top:3420px;height:380px}
.doctor h2{left:152px;top:54px;font-size:30px;font-weight:700;color:var(--navy)}
.doctor .lead{left:152px;top:100px;width:300px;font-size:11.5px;line-height:19px;color:var(--muted)}
.doc-grid{left:152px;top:155px;width:402px;height:145px;display:grid;grid-template-columns:repeat(3,1fr);grid-template-rows:repeat(2,1fr);border:1px solid var(--line)}
.doc-grid div{border:1px solid var(--line);display:flex;align-items:center;justify-content:center;font-family:"Montserrat",sans-serif;font-weight:700;font-size:14px;color:var(--navy);text-align:center}
.doc-photo{left:655px;top:22px;width:393px;height:316px;border-radius:46% 54% 50% 50% / 50% 46% 54% 50%;background:linear-gradient(135deg,#bcc6d3,#eef0f3 55%,#d6dbe2)}
.doc-dot{left:722px;top:268px;width:76px;height:76px;border-radius:50%;background:var(--yellow-soft)}

/* contact */
.contact{top:3856px;height:596px}
.contact-dome{left:60px;top:0;width:1080px;height:596px;background:var(--yellow);border-radius:540px 540px 0 0 / 360px 360px 0 0}
.contact h2{left:0;width:1200px;top:82px;text-align:center;font-size:32px;font-weight:700;color:var(--navy)}
.contact .intro{left:355px;width:490px;top:134px;text-align:center;font-size:11.5px;line-height:21px;color:#3a3000}
.field{position:absolute;height:38px;background:var(--white);border-radius:8px;font-size:11px;color:var(--muted);padding:12px 14px}
.choices h4{position:absolute;left:655px;top:253px;font-size:17px;font-weight:600;color:var(--navy)}
.check{position:absolute;display:flex;align-items:center;gap:12px;font-size:11.5px;color:#3a3000}
.check i{width:12px;height:12px;background:var(--white);border:1px solid #8a7a40}

/* footer */
.footer{top:4452px;height:371px;background:var(--navy);color:var(--white)}
.footer h4{position:absolute;top:52px;font-size:14px;font-weight:600;letter-spacing:.4px}
.footer .about{left:60px;top:116px;width:240px;font-size:11px;line-height:20px;color:#dfe6f5}
.footer .social-dot{position:absolute;left:60px;top:202px;border-color:var(--yellow)}
.finfo{position:absolute;left:369px;font-size:11px;line-height:19px;color:#e3e9f6}
.fphone{position:absolute;left:337px;display:flex;align-items:center;gap:14px;font-size:15px}
.fphone b{color:var(--yellow);font-family:"Montserrat",sans-serif;font-weight:700}
.links{position:absolute;left:612px;top:90px;list-style:none;font-size:11px;line-height:22.5px;color:#e3e9f6}
.links li::before{content:"";display:inline-block;width:5px;height:5px;border-radius:50%;background:var(--yellow);margin-right:14px;vertical-align:middle}
.refer{left:885px;top:138px;width:255px;height:40px}
.copy{position:absolute;left:0;top:318px;width:1200px;height:53px;border-top:1px solid rgba(255,255,255,.15);text-align:center;font-size:11px;line-height:53px;color:var(--yellow)}
</style>
</head>
<body>

<header class="sec topbar">
  <div class="brand" style="left:60px;top:12px"><span class="brand-square"></span><span>TALLOWMERE<br>COVER</span></div>
  <div class="abs call">
    <span class="call-icon"><svg width="16" height="16" viewBox="0 0 24 24"><path d="M6.6 10.8a15 15 0 0 0 6.6 6.6l2.2-2.2c.3-.3.7-.4 1-.2 1.1.4 2.3.6 3.6.6.6 0 1 .4 1 1V20c0 .6-.4 1-1 1A17 17 0 0 1 3 4c0-.6.4-1 1-1h3.5c.6 0 1 .4 1 1 0 1.3.2 2.5.6 3.6.1.3 0 .7-.2 1z" fill="#fcc400"/></svg></span>
    <span><small>Call Us On</small><b>800-555-0142</b></span>
  </div>
  <div class="abs langs" aria-label="Language selection">
    <svg class="lang" viewBox="0 0 30 30" role="img" aria-label="Russian"><rect width="30" height="10" fill="#fff"/><rect y="10" width="30" height="10" fill="#1c4fc4"/><rect y="20" width="30" height="10" fill="#d52b1e"/></svg>
    <svg class="lang" viewBox="0 0 30 30" role="img" aria-label="English"><rect width="30" height="30" fill="#1f3f8f"/><rect x="12" width="6" height="30" fill="#fff"/><rect y="12" width="30" height="6" fill="#fff"/><rect x="13.5" width="3" height="30" fill="#d52b1e"/><rect y="13.5" width="30" height="3" fill="#d52b1e"/></svg>
    <svg class="lang" viewBox="0 0 30 30" role="img" aria-label="Spanish"><rect width="30" height="30" fill="#c60b1e"/><rect y="8" width="30" height="14" fill="#ffc400"/></svg>
    <svg class="lang" viewBox="0 0 30 30" role="img" aria-label="Chinese"><rect width="30" height="30" fill="#de2910"/><circle cx="9" cy="9" r="3.5" fill="#ffde00"/></svg>
  </div>
</header>

<nav class="sec navbar">
  <div class="nav">
    <a class="active">Home</a><a>Individual Health</a><a>Group Health</a><a>Life Insurance</a><a>Pension &amp; Annuities</a><a>Property &amp; Commercial</a><a>Doctors Network</a><a>Contact Us</a>
  </div>
  <div class="abs nav-cta">Get An Instant Quote</div>
</nav>

<section class="sec hero">
  <div class="abs hero-glow"></div>
  <div class="abs" style="left:530px;top:-10px;width:700px;height:690px;border-radius:50%;background:var(--yellow)"></div>
  <div class="abs" role="img" aria-label="Family photo: smiling parents with two young children" style="left:528px;top:-22px;width:680px;height:675px;border-radius:50%;background:linear-gradient(135deg,#6b5a4a,#b89a7e 45%,#e7dccf 80%);border:14px solid var(--navy)"></div>
  <div class="abs" style="left:562px;top:330px;width:30px;height:30px;border-radius:50%;background:#ffe27a"></div>
  <div class="abs" style="left:926px;top:526px;width:74px;height:74px;border-radius:50%;background:#d9e4f7"></div>
  <div class="abs hero-kicker heading">Think of Your<br>Future, Think A</div>
  <h1 class="abs hero-title">SAFE FUTURE !</h1>
  <p class="abs hero-text">We aim to offer you the highest quality insurance and service on the market.</p>
  <div class="btn btn-navy" style="left:60px;top:361px;width:157px;height:38px">Contact Us <span class="arrow-ring"><svg viewBox="0 0 12 12"><path d="M1 6h9M6 2l4 4-4 4" stroke="#fcc400" stroke-width="1.8" fill="none"/></svg></span></div>
  <div class="abs follow">Follow Us <i></i><span class="social-dot" aria-label="Social page"></span></div>
</section>

<section class="abs quote">
  <span class="dot" style="left:174px"></span><span class="dot" style="left:564px"></span>
  <div class="quote-head heading"><div class="l1">CLICK HERE TO GET AN</div><div class="l2">INDIVIDUAL HEALTH INSURANCE QUOTE</div></div>
  <p>Shop Online for an affordable individual &amp; Family Health Insurance Plan. All Major Companies represented.</p>
  <div class="select">Select Your Carriers <span><svg width="14" height="10" viewBox="0 0 14 10"><path d="M2 2l5 5 5-5" stroke="#0b3c93" stroke-width="2" fill="none"/></svg></span></div>
</section>

<section class="sec welcome">
  <div class="abs w-dot1"></div>
  <div class="abs welcome-photo" role="img" aria-label="Photo: man with his dog sitting in the open boot of a car"></div>
  <div class="abs w-dot2"></div>
  <div class="abs kicker">Welcome To Visitor</div>
  <h2 class="abs">TALLOWMERE<br>COVER</h2>
  <p class="abs body" style="top:132px">Tallowmere Cover Corporation is an Independent Insurance and Financial Brokerage Firm serving clients throughout Florida and internationally. We are an experienced team of professionals, committed to our primary mission – to find the less expensive insurance coverage, for protection you want, at the best rate you deserve. Our integrated suite of online services facilitates a comprehensive search and review of leading insurance companies.</p>
  <p class="abs body" style="top:300px">Tallowmere Cover Corporation is not owned by any insurance company, therefore we provide objective information to consumers and small business owners, helping them make informed decisions about their insurance and financial needs. We aim to offer you the highest quality insurance and service on the market</p>
  <div class="btn btn-navy" style="left:691px;top:433px;width:164px;height:41px">Learn More <span class="arrow-ring"><svg viewBox="0 0 12 12"><path d="M1 6h9M6 2l4 4-4 4" stroke="#fcc400" stroke-width="1.8" fill="none"/></svg></span></div>
</section>

<section class="sec services">
  <h2 class="abs">OUR SERVICES</h2>
  <p class="abs sub">Below Are some of, The insurance services we offer:</p>

  <div class="card" style="left:176px;top:211px">
    <svg class="icon" viewBox="0 0 56 56" role="img" aria-label="Individual health icon"><circle cx="28" cy="16" r="7" fill="none" stroke="#0b3c93" stroke-width="2.5"/><path d="M14 44c2-10 8-14 14-14s12 4 14 14" fill="none" stroke="#0b3c93" stroke-width="2.5"/><path d="M6 34l10 14M50 34L40 48" stroke="#fcc400" stroke-width="3"/></svg>
    <h3>INDIVIDUAL HEALTH</h3>
    <p>For quality and affordable dental care we offer rich plans and unbeatable savings with the security.</p>
    <span class="more">Learn More</span>
  </div>
  <div class="card featured" style="left:468px;top:211px">
    <div class="icon"><svg width="46" height="46" viewBox="0 0 46 46" role="img" aria-label="Group health icon"><rect x="17" y="8" width="12" height="30" rx="2" fill="#e8453c"/><rect x="8" y="17" width="30" height="12" rx="2" fill="#e8453c"/><circle cx="8" cy="8" r="4" fill="#0b3c93"/><circle cx="38" cy="8" r="4" fill="#0b3c93"/></svg></div>
    <h3>GROUP HEALTH</h3>
    <p>For quality and affordable dental care we offer rich plans and unbeatable savings with the security.</p>
    <span class="more">Learn More</span>
  </div>
  <div class="card" style="left:760px;top:211px">
    <svg class="icon" viewBox="0 0 56 56" role="img" aria-label="Life insurance icon"><circle cx="28" cy="20" r="12" fill="#cfe27a" stroke="#0b3c93" stroke-width="2.5"/><path d="M28 32v18M20 42h16" stroke="#0b3c93" stroke-width="2.5"/></svg>
    <h3>LIFE INSURANCE</h3>
    <p>For quality and affordable dental care we offer rich plans and unbeatable savings with the security.</p>
    <span class="more">Learn More</span>
  </div>

  <div class="card" style="left:176px;top:466px">
    <svg class="icon" viewBox="0 0 56 56" role="img" aria-label="Pension and annuities icon"><circle cx="20" cy="12" r="6" fill="#e8453c"/><path d="M12 50V26h16v24" fill="#e8453c"/><path d="M34 28l10-4 10 4v10c0 6-5 10-10 12-5-2-10-6-10-12z" fill="#5d8fd8" stroke="#0b3c93" stroke-width="2"/></svg>
    <h3>PENSION &amp; ANNUITIES</h3>
    <p>For quality and affordable dental care we offer rich plans and unbeatable savings with the security.</p>
  </div>
  <div class="card" style="left:468px;top:466px">
    <svg class="icon" viewBox="0 0 56 56" role="img" aria-label="Property and commercial icon"><rect x="6" y="18" width="22" height="32" fill="#5d8fd8" stroke="#0b3c93" stroke-width="2"/><rect x="28" y="8" width="16" height="42" fill="#cfe27a" stroke="#0b3c93" stroke-width="2"/><path d="M38 30l8-3 8 3v8c0 5-4 8-8 10-4-2-8-5-8-10z" fill="#e8453c"/></svg>
    <h3>PROPERTY &amp; COMMERCIAL</h3>
    <p>For quality and affordable dental care we offer rich plans and unbeatable savings with the security.</p>
  </div>
  <div class="card" style="left:760px;top:466px">
    <svg class="icon" viewBox="0 0 56 56" role="img" aria-label="Doctors network icon"><circle cx="28" cy="12" r="7" fill="#e8453c"/><circle cx="12" cy="34" r="6" fill="#5d8fd8"/><circle cx="44" cy="34" r="6" fill="#5d8fd8"/><path d="M28 19v12M16 34h24M12 40v10M44 40v10M28 31v19" stroke="#0b3c93" stroke-width="2.5"/></svg>
    <h3>DOCTORS NETWORK</h3>
    <p>For quality and affordable dental care we offer rich plans and unbeatable savings with the security.</p>
  </div>

  <div class="abs cta-bar">
    <span style="left:98px">GET A QUOTE</span>
    <span style="left:438px">CONTACT US</span>
    <div class="or"><b>Or</b></div>
  </div>
</section>

<section class="sec carriers">
  <h2 class="abs">CLICK ON THE LINK BELOW TO APPLY<br>DIRECTLY TO YOUR PREFERRED CARRIER</h2>
  <div class="tile" style="left:176px;top:163px">Quillmarsh</div>
  <div class="tile" style="left:410px;top:161px">Kestrowan</div>
  <div class="tile" style="left:650px;top:161px">Drovenith</div>
  <div class="tile" style="left:889px;top:161px">Larkwhistle Plans</div>
  <div class="tile" style="left:292px;top:277px">Sorrelgate</div>
  <div class="tile" style="left:530px;top:277px">Pellifay Mutual</div>
  <div class="tile" style="left:769px;top:277px">Thistlecombe</div>
</section>

<section class="sec group">
  <div class="abs group-photo" role="img" aria-label="Photo: smiling doctor in white coat with a mother and child in a clinic"></div>
  <div class="abs group-card">
    <h2>GROUP HEALTH<br>INSURANCE<br>QUOTE</h2>
    <p>Health insurance is THE topic of conversation nationwide, as it impacts everyone in the workplace</p>
    <div class="btn btn-yellow" style="left:53px;top:248px;width:215px;height:40px">Group Census Form <span class="arrow-ring"><svg viewBox="0 0 12 12"><path d="M1 6h9M6 2l4 4-4 4" stroke="#0b3c93" stroke-width="1.8" fill="none"/></svg></span></div>
  </div>
</section>

<section class="sec doctor">
  <h2 class="abs">FIND A DOCTOR</h2>
  <p class="abs lead">Here to find a provider or hospital under the insurance company you prefer.</p>
  <div class="abs doc-grid">
    <div>Wimberlaine</div><div>Quillmarsh</div><div>Brackenhurl</div>
    <div>Thistlecombe</div><div>Drovenith</div><div>Kestrowan</div>
  </div>
  <div class="btn btn-navy" style="left:152px;top:321px;width:157px;height:40px">Contact Us <span class="arrow-ring"><svg viewBox="0 0 12 12"><path d="M1 6h9M6 2l4 4-4 4" stroke="#fcc400" stroke-width="1.8" fill="none"/></svg></span></div>
  <div class="abs doc-dot"></div>
  <div class="abs doc-photo" role="img" aria-label="Photo: female doctor holding a tablet in a hospital corridor"></div>
</section>

<section class="sec contact">
  <div class="abs contact-dome"></div>
  <h2 class="abs">CONTACT US</h2>
  <p class="abs intro">If you have any questions concerning insurance, please fill out the form and a representative will get back to you by the next business day, or feel free to call 800-555-0142.</p>
  <div class="field" style="left:198px;top:234px;width:204px">Name *</div>
  <div class="field" style="left:415px;top:234px;width:206px">Email *</div>
  <div class="field" style="left:198px;top:285px;width:204px">Phone *</div>
  <div class="field" style="left:415px;top:285px;width:206px">Business</div>
  <div class="field" style="left:198px;top:337px;width:423px">Address</div>
  <div class="field" style="left:198px;top:386px;width:423px;height:82px">Comments / Questions:</div>
  <div class="btn btn-navy" style="left:198px;top:478px;width:122px;height:39px">Submit <span class="arrow-ring"><svg viewBox="0 0 12 12"><path d="M1 6h9M6 2l4 4-4 4" stroke="#fcc400" stroke-width="1.8" fill="none"/></svg></span></div>

  <div class="choices">
    <h4>Type Of Coverage Interested In:</h4>
    <label class="check" style="left:659px;top:297px"><i></i>Annuities</label>
    <label class="check" style="left:854px;top:297px"><i></i>Individual Health</label>
    <label class="check" style="left:659px;top:328px"><i></i>International Health</label>
    <label class="check" style="left:854px;top:328px"><i></i>Group Health Life</label>
    <label class="check" style="left:659px;top:358px"><i></i>Life Insurance</label>
    <label class="check" style="left:854px;top:358px"><i></i>Auto</label>
    <label class="check" style="left:659px;top:388px"><i></i>Homeowners</label>
    <label class="check" style="left:854px;top:388px"><i></i>Commercial</label>
    <label class="check" style="left:659px;top:418px"><i></i>Medicare Supplements</label>
    <label class="check" style="left:854px;top:418px"><i></i>Dental / Ancillary Products</label>
  </div>
</section>

<footer class="sec footer">
  <div class="brand" style="left:60px;top:44px"><span class="brand-square"></span><span>TALLOWMERE<br>COVER</span></div>
  <p class="abs about">We listen to our clients and are happy to discuss any issues or concerns you may have with your policy.</p>
  <span class="social-dot" aria-label="Social page"></span>

  <h4 style="left:337px">CONTACT INFO</h4>
  <svg class="abs" style="left:337px;top:92px" width="18" height="22" viewBox="0 0 18 22"><path d="M9 1a7 7 0 0 1 7 7c0 5-7 13-7 13S2 13 2 8a7 7 0 0 1 7-7z" fill="#fcc400"/><circle cx="9" cy="8" r="2.5" fill="#0b3c93"/></svg>
  <p class="finfo" style="top:92px">Tallowmere Cover<br>410 Harbor Crest Ave –<br>Suite 210 Seabrook Shores,<br>FL 30001</p>
  <div class="fphone" style="top:180px"><svg width="16" height="16" viewBox="0 0 24 24"><path d="M6.6 10.8a15 15 0 0 0 6.6 6.6l2.2-2.2c.3-.3.7-.4 1-.2 1.1.4 2.3.6 3.6.6.6 0 1 .4 1 1V20c0 .6-.4 1-1 1A17 17 0 0 1 3 4c0-.6.4-1 1-1h3.5c.6 0 1 .4 1 1 0 1.3.2 2.5.6 3.6.1.3 0 .7-.2 1z" fill="#fcc400"/></svg><b>800-555-0142</b><small style="font-size:11px;color:var(--yellow)">(Toll Free)</small></div>
  <div class="fphone" style="top:212px"><svg width="16" height="16" viewBox="0 0 24 24"><path d="M6.6 10.8a15 15 0 0 0 6.6 6.6l2.2-2.2c.3-.3.7-.4 1-.2 1.1.4 2.3.6 3.6.6.6 0 1 .4 1 1V20c0 .6-.4 1-1 1A17 17 0 0 1 3 4c0-.6.4-1 1-1h3.5c.6 0 1 .4 1 1 0 1.3.2 2.5.6 3.6.1.3 0 .7-.2 1z" fill="#fcc400"/></svg>555-201-4477</div>
  <div class="fphone" style="top:248px"><svg width="16" height="16" viewBox="0 0 24 24"><rect x="4" y="9" width="16" height="9" rx="2" fill="#fcc400"/><rect x="7" y="3" width="10" height="6" fill="#fcc400"/><rect x="7" y="15" width="10" height="6" fill="#fff"/></svg>555-201-4490</div>

  <h4 style="left:612px">QUICK LINKS</h4>
  <ul class="links">
    <li>Home</li><li>Property &amp; Commercial</li><li>Individual Health</li><li>Doctors Network</li><li>Group Health</li><li>Get an Instant Quote</li><li>Life Insurance</li><li>Pension &amp; Annuities</li><li>Contact Us</li>
  </ul>

  <div class="btn btn-yellow refer">Refer Us To Your Friends <span class="arrow-ring"><svg viewBox="0 0 12 12"><path d="M1 6h9M6 2l4 4-4 4" stroke="#0b3c93" stroke-width="1.8" fill="none"/></svg></span></div>

  <div class="copy">©Tallowmere Cover - 2021 All rights reserved.</div>
</footer>

</body>
</html>
```